#28 - On the Letterheadpaper, can you please make the footercolorfields littlebit darker? I mean the Colors are too bright compared to the Logocolors, or?!
@Torven #22 - Can you please add on the backside the url's like on #7 ?
@quembrastudio #18 - Businesscard: The footer (colored fields) maybe a little bit to strong/high, can you test it with 2-3px less? #18 - Letterheadpaper: Need the footer (colored fields) here! Looks without ... nacked. ;) #18 - Please add the "Back of the business card"-things what you can read in the briefing.
@quembrastudio #1#2 - Eliminated; Better draft available with #4 #11 - Eliminated; I think the logo is better on a "normal" business card style, and maybe thats are other card Dimensions. #10 #9 - The Black Symbols on the Businesscard is maybe to strong. Can you test it with blue or grey symbols? #4 - At the moment my favorite, but please the "84116 Grunwiesel" in a new line under the Street (businesscard), thats the correct format in Germany. I'm not so happy with the URL in the blue footerfield, maybe smaller or in a other location, I don't know?! Please put on the letterhead the Facts from the footer into the header (right under the Logo), maybe in a small/tiny clear Fonttype. The Flyerbusinesscard don't have the color fields on the bottom?
@torven #8 - Front looks nice, but the Logo on the backside is not strong/"clear" enough I think. #7#5 - Eliminated; Not my Style, Sorry. #6 - Eliminated; The footer (blue field) on the Front was to heavy
Can't vote for your drafts the Flyer and Letterhead are missing.
@vOlpt
Nice blue symbols on the Businesscard, but the color on the backside is purple, I think that kills the blue/grey Logo and Style on the Frontside. And the Logo with Name under it is one unit, either the Logo with the Name direct under the Logo, or the Logo standalone. :)
Cant't vote for your drafts, don't need Envelopes but the Flyer. ;)
@Marble314
Thanks for your Drafts, but it's not my Style and I think it's not the Style from the Logo, the heavy yellow Background "kills" the nice look of the Blue/Grey Logo, too.
#2 In Germany is it more standard that the Logo is on the right side.
Please make a new draft with the Logo on the right side and the personal data (Address) under the Logo. In the footer comes the web address and maybe later some bank account informations or a funny quote.
I miss in the Address the ID and the Name of the City (I forget it in the briefing, Sorry) please add it to the drafts.
=> "84116 Grunwiesel"
The Name under the Logo ("Lukas Wendorf") looks like a little to big/wide on the right side, please let it start and end on the exact same width that the Logo is.
The "Background" of the Flyer with the integrated Business Card can't be complete blue, there will be some Text added in the future, it's a information Flyer with some facts about my work and so on, so there must be some space for these texts. The Businesscard "in" the Flyer must the same Card as the normal Business card, except the round corners.
The Dimensions from all the stuff is like the given Dimensions from the attached Information-PDF's?
OK, the price is guaranteed! I would upgrade this project, the Problem is I must pay with coinrelay, and in Germany you send via echeck the money from your regular bank account to coinrelay. But this way need very very long here on zentrofix.example (I don't know why), i paid this project on the 16. feb, today (25. fe) the project started, ~7 workdays for clearing the echeck. So, when I now pay the Guaranteed-Upgrade the project-option will confirmed when the project ends ...
The Logo itself comes from my first project here on zentrofix.example, and there was the price guaranteed, too.
#22 - Can you please add on the backside the url's like on #7 ?
@quembrastudio
#18 - Businesscard: The footer (colored fields) maybe a little bit to strong/high, can you test it with 2-3px less?
#18 - Letterheadpaper: Need the footer (colored fields) here! Looks without ... nacked. ;)
#18 - Please add the "Back of the business card"-things what you can read in the briefing.
#1 #2 - Eliminated; Better draft available with #4
#11 - Eliminated; I think the logo is better on a "normal" business card style, and maybe thats are other card Dimensions.
#10 #9 - The Black Symbols on the Businesscard is maybe to strong. Can you test it with blue or grey symbols?
#4 - At the moment my favorite, but please the "84116 Grunwiesel" in a new line under the Street (businesscard), thats the correct format in Germany. I'm not so happy with the URL in the blue footerfield, maybe smaller or in a other location, I don't know?! Please put on the letterhead the Facts from the footer into the header (right under the Logo), maybe in a small/tiny clear Fonttype. The Flyerbusinesscard don't have the color fields on the bottom?
@torven
#8 - Front looks nice, but the Logo on the backside is not strong/"clear" enough I think.
#7 #5 - Eliminated; Not my Style, Sorry.
#6 - Eliminated; The footer (blue field) on the Front was to heavy
So, trust me or not.
--- Gerold

```html
<!DOCTYPE html>
<html lang="de">
<head>
<meta charset="utf-8">
<title>Lukas Wendorf – Geschäftsausstattung</title>
<link rel="stylesheet" href="https://fonts.googleapis.com/css2?family=Open+Sans:wght@400;600;700&display=swap">
<style>
  :root{
    --stage:#e6e2da;
    --paper:#ffffff;
    --brand-blue:#1b5fcf;
    --brand-blue-dark:#0f3f95;
    --brand-grey:#4f5155;
    --text:#3a3c40;
    --muted:#8a8d92;
    --edge:#d3d0ca;
  }
  *{box-sizing:border-box;margin:0;padding:0}
  html,body{width:1200px;height:927px;overflow:hidden}
  body{background:var(--stage);font-family:"Open Sans",Arial,sans-serif;color:var(--text);position:relative}
  .sheet{position:absolute;background:var(--paper);box-shadow:0 3px 10px rgba(0,0,0,.18);overflow:hidden}

  .wordmark{font-weight:700;color:var(--brand-blue);white-space:nowrap;line-height:1}

  /* Letterhead */
  .letterhead{left:55px;top:168px;width:446px;height:629px}
  .letterhead .head{position:absolute;left:320px;top:18px;width:110px}
  .letterhead .wordmark{font-size:13px}
  .letterhead .details{margin-top:8px;font-size:6px;line-height:1.5;color:var(--text)}
  .footer-bars{position:absolute;left:0;right:0;bottom:0;height:12px;display:flex;gap:4px}
  .footer-bars .blue{flex:0 0 69%;background:var(--brand-blue)}
  .footer-bars .grey{flex:1;background:var(--brand-grey)}

  /* Business card front */
  .card-front{left:401px;top:346px;width:315px;height:180px}
  .card-front .name{position:absolute;left:22px;top:28px;font-size:13px;font-weight:700;color:var(--brand-blue)}
  .card-front .mark{position:absolute;right:18px;top:22px;font-size:11px}
  .card-front .address{position:absolute;left:168px;top:58px;font-size:6.5px;line-height:1.5}
  .card-front .url{position:absolute;left:22px;top:146px;font-size:7px}
  .card-front .footer-bars{height:8px}

  /* Business card back */
  .card-back{left:401px;top:541px;width:315px;height:180px;
    background:radial-gradient(ellipse at 50% 30%,#3f86e8 0%,var(--brand-blue) 45%,var(--brand-blue-dark) 100%)}
  .card-back .faint{position:absolute;left:0;right:0;top:64px;text-align:center;font-size:22px;font-weight:700;color:rgba(255,255,255,.35)}
  .card-back .links{position:absolute;left:0;right:0;top:142px;text-align:center;font-size:6px;line-height:1.6;color:rgba(255,255,255,.85)}

  /* Envelopes */
  .envelope-large{left:734px;top:456px;width:248px;height:361px}
  .envelope-small{left:904px;top:145px;width:253px;height:281px}
  .window{position:absolute;border:1px solid var(--edge);border-radius:10px;background:#fbfbfb}
  .envelope-large .window{left:40px;top:95px;width:90px;height:150px}
  .envelope-small .window{left:95px;top:60px;width:80px;height:125px}
  .rotated{position:absolute;left:50%;top:50%;transform:translate(-50%,-50%) rotate(-90deg);text-align:left;white-space:nowrap}
  .rotated .wordmark{font-size:12px}
  .rotated .details{margin-top:5px;font-size:5px;line-height:1.5;color:var(--muted)}
</style>
</head>
<body>

<section class="sheet letterhead" aria-label="Briefbogen">
  <div class="head">
    <div class="wordmark">Lukas Wendorf</div>
    <div class="details">
      Lindenweg 14<br>
      84116 Grunwiesel<br>
      Call: 0871 / 552014<br>
      Fax: 0871 / 552015<br>
      Email: mail@lukaswendorf.example
    </div>
  </div>
  <div class="footer-bars"><span class="blue"></span><span class="grey"></span></div>
</section>

<section class="sheet card-front" aria-label="Visitenkarte Vorderseite">
  <div class="name">Lukas Wendorf</div>
  <div class="wordmark mark">Lukas Wendorf</div>
  <div class="address">
    Lindenweg 14<br>
    84116 Grunwiesel<br><br>
    Call: 0871 / 552014<br>
    Fax: 0871 / 552015<br>
    Email: mail@lukaswendorf.example
  </div>
  <div class="url">www.lukaswendorf.example</div>
  <div class="footer-bars"><span class="blue"></span><span class="grey"></span></div>
</section>

<section class="sheet card-back" aria-label="Visitenkarte Rückseite">
  <div class="faint">Lukas Wendorf</div>
  <div class="links">
    video.example/lukaswendorf | social.example/lukaswendorf<br>
    chat.example/lukaswendorf | photo.example/lukaswendorf
  </div>
</section>

<section class="sheet envelope-large" aria-label="Umschlag groß">
  <div class="window">
    <div class="rotated">
      <div class="wordmark">Lukas Wendorf</div>
      <div class="details">Lindenweg 14 · 84116 Grunwiesel<br>www.lukaswendorf.example</div>
    </div>
  </div>
</section>

<section class="sheet envelope-small" aria-label="Umschlag klein">
  <div class="window">
    <div class="rotated">
      <div class="wordmark">Lukas Wendorf</div>
      <div class="details">Lindenweg 14<br>84116 Grunwiesel</div>
    </div>
  </div>
</section>

</body>
</html>
```